BirchLane Hotel
BUSINESS CARDS, LETTERHEAD, ENVELOPES, FAX COVER, EMAIL SIGNATURE, signage, car
BirchLane Hotel - Hospitality Industry
Creative Brief
Simple
DOHYUN KWAK
President & C.E.O
B2 Sora Bldg. 412-5 Mokhwa-dong, Seocho-gu, Seoul, 137-914, Korea
oliver@blhotelgroup.com
www.blhotelgroup.com
BirchLane Pohang: 218-4 Hwajin-dong, Bukgu, Pohang, Korea BirchLane Gunsan: 457 Maeryeong-dong, Gunsan, Korea

```html
<!DOCTYPE html>
<html lang="en">
<head>
<meta charset="UTF-8">
<title>BirchLane Hotel – Business Card</title>
<link href="https://fonts.googleapis.com/css2?family=Arimo:wght@400;700&display=swap" rel="stylesheet">
<style>
  :root {
    --stage: #6f7772;
    --card-white: #ffffff;
    --leaf: #8cc63f;
    --leaf-light: #a3d45f;
    --leaf-deep: #5f9a26;
    --ink-light: #ffffff;
  }
  * { margin: 0; padding: 0; box-sizing: border-box; }
  html, body { width: 1200px; height: 850px; overflow: hidden; }
  body {
    background: var(--stage);
    font-family: "Arimo", Arial, sans-serif;
    position: relative;
  }
  .card {
    position: absolute;
    top: 312px;
    width: 422px;
    height: 240px;
    box-shadow: 0 2px 6px rgba(0,0,0,0.25);
    overflow: hidden;
  }
  .card--front { left: 149px; background: var(--card-white); }
  .card--back { left: 610px; }

  .pattern {
    position: absolute;
    inset: 0;
    background:
      radial-gradient(circle at 80% 20%, var(--leaf-light) 0, transparent 35%),
      radial-gradient(circle at 30% 85%, var(--leaf-light) 0, transparent 30%),
      var(--leaf);
  }
  .card--front .pattern { left: 235px; }

  .brand {
    position: absolute;
    left: 0; top: 0;
    width: 235px; height: 240px;
    display: flex;
    flex-direction: column;
    align-items: center;
    justify-content: center;
    gap: 14px;
  }
  .brand__dot {
    width: 62px; height: 62px;
    border-radius: 50%;
    background: var(--leaf);
  }
  .brand__name {
    font-weight: 700;
    font-size: 17px;
    color: var(--leaf-deep);
    letter-spacing: 0.2px;
  }

  .contact {
    position: absolute;
    color: var(--ink-light);
    font-size: 7.5px;
    line-height: 1.45;
  }
  .contact--person { left: 259px; top: 56px; }
  .person__name { font-size: 12px; font-weight: 700; letter-spacing: 0.3px; line-height: 1.2; }
  .person__title { font-size: 8px; margin-bottom: 8px; }
  .person__lines { margin-bottom: 6px; }
  .person__web { position: absolute; left: 259px; top: 191px; color: var(--ink-light); font-size: 8.5px; font-weight: 700; }

  .branch { position: absolute; left: 33px; color: var(--ink-light); font-size: 7.5px; line-height: 1.45; }
  .branch--gunsan { top: 35px; }
  .branch--pohang { top: 152px; }
  .branch__name { font-size: 9px; font-weight: 700; margin-bottom: 2px; }
</style>
</head>
<body>
  <section class="card card--front">
    <div class="brand">
      <div class="brand__dot"></div>
      <div class="brand__name">BirchLane Hotel</div>
    </div>
    <div class="pattern" role="img" aria-label="Faint floral leaf pattern on green"></div>
    <div class="contact contact--person">
      <div class="person__name">DOHYUN KWAK</div>
      <div class="person__title">President &amp; C.E.O</div>
      <div class="person__lines">
        tel: (02) 3481-5520<br>
        fax: (02) 3481-5521<br>
        cell: 010-4172-3306<br>
        email: oliver@blhotelgroup.com
      </div>
      <div class="person__address">
        B2 Sora Bldg. 412-5 Mokhwa-dong,<br>
        Seocho-gu, Seoul, 137-914, Korea
      </div>
    </div>
    <div class="person__web">www.blhotelgroup.com</div>
  </section>

  <section class="card card--back">
    <div class="pattern" role="img" aria-label="Floral leaf and star pattern on green"></div>
    <div class="branch branch--gunsan">
      <div class="branch__name">BirchLane Gunsan:</div>
      457 Maeryeong-dong, Gunsan, Korea<br>
      tel: (063) 462-7180
    </div>
    <div class="branch branch--pohang">
      <div class="branch__name">BirchLane Pohang:</div>
      218-4 Hwajin-dong, Bukgu, Pohang, Korea<br>
      tel: (054) 248-3915
    </div>
  </section>
</body>
</html>
```